Audio and Video download site

I am looking for a good and beautiful website where users can be a able to download and upload musicial files and video file. Basically, there will be two categories. The first category for the music files( mp3, mva and other popular music files) while the second category will be for video files (mp4, wmv, divx and other files) users would be able to like and dislike a song/video. Users do not necessarily have to sign up for them to make you or download and upload files from the website. The website should be youthful.

```html
<!DOCTYPE html>
<html lang="en">
<head>
<meta charset="utf-8">
<title>VIBRA – Music and Video Files</title>
<link href="https://fonts.googleapis.com/css2?family=Open+Sans:wght@400;600;700&display=swap" rel="stylesheet">
<style>
:root{
  --accent:#f2522e;
  --accent-dark:#d9431f;
  --ink:#ffffff;
  --muted:#bdbdbd;
  --dim:#8a8a8a;
  --bg-welcome:#1b1b1b;
  --bg-album:#1c1c1c;
  --bg-video:#050505;
  --bg-footer:#171717;
  --row:#3a3a3a;
  --card-dark:#2a2a2a;
  --paper:#ffffff;
  --paper-text:#555555;
}
*{box-sizing:border-box;margin:0;padding:0}
html,body{width:1200px;height:2782px;overflow:hidden}
body{font-family:"Open Sans",Arial,sans-serif;color:var(--ink);background:#000;position:relative}
.section{position:absolute;left:0;width:1200px}
.accent{color:var(--accent)}
.icon{display:inline-block;vertical-align:middle;fill:currentColor}
.section-title{position:absolute;left:0;width:1200px;text-align:center;font-size:26px;font-weight:600;letter-spacing:.3px}

/* hero */
.hero{top:0;height:542px;overflow:hidden}
.hero-photo{position:absolute;inset:0;background:
  radial-gradient(ellipse at 78% 18%,rgba(240,225,200,.75),rgba(0,0,0,0) 45%),
  radial-gradient(ellipse at 35% 55%,#5a3d33 0%,rgba(0,0,0,0) 45%),
  linear-gradient(100deg,#2a1d22 0%,#4b3a3a 35%,#7a7068 60%,#4c4a48 85%,#2e2c2c 100%)}
.hero-shade{position:absolute;inset:0;background:linear-gradient(180deg,rgba(0,0,0,.25),rgba(0,0,0,.1) 40%,rgba(0,0,0,.35))}
.nav{position:absolute;top:0;left:0;width:1200px;height:100px}
.nav a{position:absolute;top:41px;font-size:13px;font-weight:600;color:var(--ink);text-decoration:none;text-transform:uppercase;transform:translateX(-50%);white-space:nowrap}
.nav a.active{color:var(--accent)}
.brand{position:absolute;top:32px;left:551px;transform:translateX(-50%)}
.brand-name{font-size:26px;font-weight:600;color:var(--ink);letter-spacing:.5px;line-height:36px}
.search{position:absolute;left:1062px;top:31px;width:38px;height:38px;border-radius:50%;background:var(--accent);display:flex;align-items:center;justify-content:center}
.slide-arrow{position:absolute;top:259px;width:38px;height:38px;border-radius:50%;border:1px solid rgba(255,255,255,.45);background:rgba(0,0,0,.25);display:flex;align-items:center;justify-content:center}
.hero-title{position:absolute;top:270px;left:500px;width:625px;text-align:center;font-size:33px;font-weight:400;letter-spacing:.5px}
.hero-sub{position:absolute;top:334px;left:500px;width:625px;text-align:center;font-size:20px;font-weight:600;text-transform:uppercase;letter-spacing:.2px}

/* welcome */
.welcome{top:542px;height:530px;background:var(--bg-welcome)}
.welcome .section-title{top:58px}
.welcome-text{position:absolute;top:105px;left:190px;width:820px;text-align:center;font-size:11.5px;line-height:21px;color:#e0e0e0}
.category{position:absolute;top:178px;width:488px;height:284px;border:2px solid #e8e8e8;overflow:hidden;text-align:center}
.category.music{left:98px}
.category.video{left:614px}
.category-photo{position:absolute;inset:0}
.music .category-photo{background:radial-gradient(ellipse at 30% 25%,#4c6a70,rgba(0,0,0,0) 55%),linear-gradient(160deg,#1f3540,#101a20 60%,#27221f)}
.video .category-photo{background:radial-gradient(ellipse at 55% 20%,#5b5e78,rgba(0,0,0,0) 55%),linear-gradient(160deg,#3a3036,#5a3a3a 55%,#241c1e)}
.category-photo::after{content:"";position:absolute;inset:0;background:rgba(0,0,0,.35)}
.category h3{position:relative;margin-top:50px;font-size:26px;font-weight:400;text-transform:uppercase}
.category p{position:relative;margin:12px auto 0;width:300px;font-size:15.5px;line-height:26px;color:#e6e6e6}
.actions{position:absolute;top:179px;left:45px;display:flex;gap:17px}
.btn{width:189px;height:43px;display:flex;align-items:center;justify-content:space-between;padding:0 20px;font-size:15px;text-transform:uppercase;color:var(--ink)}
.btn-solid{background:var(--accent)}
.btn-line{border:1px solid #e0e0e0;background:rgba(0,0,0,.25);padding-left:36px}

/* music list */
.music-files{top:1072px;height:505px;overflow:hidden}
.crowd{position:absolute;inset:0;background:
  radial-gradient(ellipse at 40% 20%,#9a9a9a,rgba(0,0,0,0) 40%),
  radial-gradient(ellipse at 80% 30%,#777,rgba(0,0,0,0) 35%),
  linear-gradient(180deg,#3d3d3d,#1e1e1e 55%,#0c0c0c)}
.music-files .heading{position:absolute;left:98px;top:64px;font-size:26px;font-weight:600;text-transform:uppercase}
.track{position:absolute;left:98px;width:876px;height:50px;display:flex;align-items:center;background:rgba(70,70,70,.85)}
.track .note{width:62px;display:flex;justify-content:center;color:var(--accent)}
.track-info{width:226px}
.track-name{font-size:15px;line-height:18px}
.track-artist{font-size:11px;color:#d0d0d0;display:flex;align-items:center;gap:6px;margin-left:10px}
.track .sep{width:1px;height:36px;background:#777}
.fmt{font-size:13px;color:#dcdcdc}
.track-votes{position:absolute;right:0;top:0;height:50px;width:258px;background:var(--accent);display:flex;align-items:center;justify-content:space-around;padding:0 6px;font-size:11.5px;text-transform:uppercase}
.track-votes span{display:flex;align-items:center;gap:4px}
.view-more{position:absolute;font-size:16px;color:var(--accent)}

/* album */
.albums{top:1577px;height:380px;background:var(--bg-album)}
.albums .section-title{top:60px}
.album{position:absolute;top:124px;width:238px;height:184px;background:var(--card-dark)}
.album-photo{height:137px}
.album:nth-of-type(1) .album-photo{background:linear-gradient(160deg,#5a4a3c,#2a2420 60%,#6d2a22)}
.album:nth-of-type(2) .album-photo{background:linear-gradient(160deg,#7a6a58,#4a3a30 50%,#2a2522)}
.album:nth-of-type(3) .album-photo{background:radial-gradient(ellipse at 50% 60%,#c5231e,rgba(0,0,0,0) 40%),linear-gradient(160deg,#c9a046,#5a4022 60%,#2e2418)}
.album:nth-of-type(4) .album-photo{background:radial-gradient(ellipse at 70% 40%,#d27aa0,rgba(0,0,0,0) 45%),linear-gradient(160deg,#5a2a48,#2a1a2c 60%,#402a2a)}
.album-caption{height:47px;display:flex;align-items:center;justify-content:space-between;padding:0 10px 0 11px;font-size:15.5px}
.album-count{font-size:10px;color:var(--dim);display:flex;align-items:center;gap:4px}

/* video */
.videos{top:1957px;height:501px;background:var(--bg-video)}
.videos .section-title{top:62px}
.vcard{position:absolute;background:var(--paper);color:var(--paper-text)}
.vcard-photo{position:absolute}
.vcard h4{font-size:17px;font-weight:400;color:#333;line-height:25px}
.vmeta{display:flex;align-items:center;gap:8px;font-size:10px;color:#9a9a9a;text-transform:uppercase;margin:6px 0}
.vmeta .votes{color:var(--accent);display:flex;gap:6px}
.vtext{font-size:11.5px;line-height:19px;color:#666}
.tags{display:flex;gap:3px}
.tags span{background:var(--accent);color:#fff;font-size:10px;padding:2px 4px}
.vdl{color:var(--accent);font-size:15.5px;text-transform:uppercase;display:flex;align-items:center;gap:10px}
.vcard.big{left:98px;top:121px;width:496px;height:274px}
.vcard.big .vcard-photo{left:10px;top:9px;width:263px;height:254px;background:radial-gradient(ellipse at 40% 30%,#e6e0d6,rgba(0,0,0,0) 40%),linear-gradient(160deg,#8a8276,#3a3632 60%,#1e1c1a)}
.vcard.big .vbody{position:absolute;left:307px;top:26px;width:172px}
.vcard.big .tags{margin-top:12px}
.vcard.big .vdl{margin-top:14px}
.vcard.small{left:614px;width:488px;height:126px}
.vcard.small .vcard-photo{left:9px;top:9px;width:131px;height:108px}
.vcard.small.one .vcard-photo{background:radial-gradient(ellipse at 40% 40%,#e8cfb6,rgba(0,0,0,0) 45%),linear-gradient(160deg,#f0e4d4,#b49478)}
.vcard.small.two .vcard-photo{background:radial-gradient(ellipse at 60% 45%,#c79a86,rgba(0,0,0,0) 45%),linear-gradient(160deg,#3a3436,#6a6060)}
.vcard.small .vbody{position:absolute;left:152px;top:4px;width:326px}
.vcard.small .vmeta{margin:2px 0}
.vcard.small .vtext{line-height:17px}
.vcard.small .vrow{display:flex;align-items:center;gap:30px;margin-top:4px}
.vcard.small .vdl{font-size:14px;gap:6px}

/* footer */
.footer{top:2458px;height:324px;background:var(--bg-footer)}
.footer-nav{position:absolute;top:60px;left:0;width:1200px;display:flex;justify-content:center;font-size:12.5px;text-transform:uppercase}
.footer-nav a{color:var(--ink);text-decoration:none;padding:0 15px}
.footer-nav i{font-style:normal;color:#aaa}
.social{position:absolute;top:119px;left:0;width:1200px;display:flex;justify-content:center;gap:28px}
.social span{width:70px;height:70px;border-radius:50%;border:3px solid #fff}
.copyright{position:absolute;top:238px;left:0;width:1200px;text-align:center;font-size:12.5px;color:#555}
.footer-line{position:absolute;bottom:0;left:0;width:1200px;height:6px;background:var(--accent)}
</style>
</head>
<body>
<svg width="0" height="0" style="position:absolute">
  <defs>
    <symbol id="i-note" viewBox="0 0 24 24"><path d="M9 3l12-2v15.5a3.5 3.5 0 1 1-2-3.2V6.3L11 7.6v11A3.5 3.5 0 1 1 9 15.3z"/></symbol>
    <symbol id="i-mic" viewBox="0 0 24 24"><rect x="8" y="2" width="8" height="13" rx="4"/><path d="M5 11h2a5 5 0 0 0 10 0h2a7 7 0 0 1-6 6.9V21h-2v-3.1A7 7 0 0 1 5 11z"/></symbol>
    <symbol id="i-down" viewBox="0 0 24 24"><path d="M10 2h4v9h4l-6 7-6-7h4z"/><path d="M2 17h3v3h14v-3h3v6H2z"/></symbol>
    <symbol id="i-up" viewBox="0 0 24 24"><path d="M12 2l6 7h-4v8h-4V9H6z"/><path d="M2 17h3v3h14v-3h3v6H2z"/></symbol>
    <symbol id="i-like" viewBox="0 0 24 24"><path d="M2 10h4v12H2zM8 21V10l5-8c2 0 3 1 2.5 3L14 9h6a2 2 0 0 1 2 2.3l-1.6 8A2 2 0 0 1 18.4 21z"/></symbol>
    <symbol id="i-dislike" viewBox="0 0 24 24"><path d="M2 2h4v12H2zM8 3v11l5 8c2 0 3-1 2.5-3L14 15h6a2 2 0 0 0 2-2.3l-1.6-8A2 2 0 0 0 18.4 3z"/></symbol>
    <symbol id="i-cam" viewBox="0 0 24 24"><rect x="1" y="6" width="15" height="12" rx="2"/><path d="M17 10l6-4v12l-6-4z"/></symbol>
    <symbol id="i-user" viewBox="0 0 24 24"><circle cx="12" cy="7" r="5"/><path d="M2 23a10 8 0 0 1 20 0z"/></symbol>
  </defs>
</svg>

<header class="section hero">
  <div class="hero-photo" role="img" aria-label="Bearded man in headphones holding a tablet on a city rooftop at sunset"></div>
  <div class="hero-shade"></div>
  <nav class="nav">
    <a class="active" href="#" style="left:139px">Home</a>
    <a href="#" style="left:269px">About Us</a>
    <a href="#" style="left:421px">Music Album</a>
    <div class="brand"><span class="brand-name">VIBRA</span></div>
    <a href="#" style="left:683px">Video Album</a>
    <a href="#" style="left:831px">Gallery</a>
    <a href="#" style="left:972px">Contact Us</a>
    <span class="search"><svg class="icon" width="18" height="18" viewBox="0 0 24 24"><circle cx="10" cy="10" r="6.5" fill="none" stroke="#fff" stroke-width="3"/><path d="M15 15l6 6" stroke="#fff" stroke-width="3.5" stroke-linecap="round"/></svg></span>
  </nav>
  <span class="slide-arrow" style="left:33px"><svg width="12" height="12" viewBox="0 0 12 12"><path d="M8 2L4 6l4 4" fill="none" stroke="#fff" stroke-width="1.6"/></svg></span>
  <span class="slide-arrow" style="left:1130px"><svg width="12" height="12" viewBox="0 0 12 12"><path d="M4 2l4 4-4 4" fill="none" stroke="#fff" stroke-width="1.6"/></svg></span>
  <h1 class="hero-title">VIBRA FOR MUSIC AND VIDEOS</h1>
  <p class="hero-sub">Download and upload musical files and video file</p>
</header>

<section class="section welcome">
  <h2 class="section-title">WELCOME TO <span class="accent">VIBRA</span></h2>
  <p class="welcome-text">Sed ut perspiciatis unde omnis iste natus error sit voluptatem accusantium doloremque laudantium, totam rem aperiam, eaque ipsa quae ab<br>illo inventore veritatis et quasi architecto beatae vitae dicta sunt explicabo. Nemo enim ipsam voluptatem quia voluptas sit aspernatur</p>
  <div class="category music">
    <div class="category-photo" role="img" aria-label="Musician at a keyboard under blue stage light"></div>
    <h3>Musical Files</h3>
    <p>You can download or upload your favrouite music files here</p>
    <div class="actions">
      <span class="btn btn-solid">Download <svg class="icon" width="16" height="16"><use href="#i-down"/></svg></span>
      <span class="btn btn-line">Upload <svg class="icon" width="16" height="16"><use href="#i-up"/></svg></span>
    </div>
  </div>
  <div class="category video">
    <div class="category-photo" role="img" aria-label="Young couple watching a video on a phone"></div>
    <h3>Video Files</h3>
    <p>You can download or upload your favrouite Video files here</p>
    <div class="actions">
      <span class="btn btn-solid">Download <svg class="icon" width="16" height="16"><use href="#i-down"/></svg></span>
      <span class="btn btn-line">Upload <svg class="icon" width="16" height="16"><use href="#i-up"/></svg></span>
    </div>
  </div>
</section>

<section class="section music-files">
  <div class="crowd" role="img" aria-label="Concert crowd with raised hands in black and white"></div>
  <h2 class="heading">Music Files of <span class="accent">VIBRA</span></h2>

  <div class="track" style="top:124px">
    <span class="note"><svg class="icon" width="22" height="22"><use href="#i-note"/></svg></span>
    <div class="track-info"><div class="track-name">Nihil molestiae consequatur</div><div class="track-artist"><svg class="icon" width="9" height="9"><use href="#i-mic"/></svg>J. Marlow</div></div>
    <span class="sep"></span>
    <span class="fmt" style="margin-left:20px">Mp3</span><span class="fmt" style="margin-left:37px">mva</span><span class="fmt" style="margin-left:37px">Other popular music files</span>
    <div class="track-votes"><span><svg class="icon" width="11" height="11"><use href="#i-like"/></svg>Like</span><span><svg class="icon" width="11" height="11"><use href="#i-dislike"/></svg>Dislike</span><span><svg class="icon" width="11" height="11"><use href="#i-down"/></svg>Download</span></div>
  </div>
  <div class="track" style="top:195px">
    <span class="note"><svg class="icon" width="22" height="22"><use href="#i-note"/></svg></span>
    <div class="track-info"><div class="track-name">Nihil molestiae consequatur</div><div class="track-artist"><svg class="icon" width="9" height="9"><use href="#i-mic"/></svg>J. Marlow</div></div>
    <span class="sep"></span>
    <span class="fmt" style="margin-left:20px">Mp3</span><span class="fmt" style="margin-left:37px">mva</span><span class="fmt" style="margin-left:37px">Other popular music files</span>
    <div class="track-votes"><span><svg class="icon" width="11" height="11"><use href="#i-like"/></svg>Like</span><span><svg class="icon" width="11" height="11"><use href="#i-dislike"/></svg>Dislike</span><span><svg class="icon" width="11" height="11"><use href="#i-down"/></svg>Download</span></div>
  </div>
  <div class="track" style="top:266px">
    <span class="note"><svg class="icon" width="22" height="22"><use href="#i-note"/></svg></span>
    <div class="track-info"><div class="track-name">Nihil molestiae consequatur</div><div class="track-artist"><svg class="icon" width="9" height="9"><use href="#i-mic"/></svg>J. Marlow</div></div>
    <span class="sep"></span>
    <span class="fmt" style="margin-left:20px">Mp3</span><span class="fmt" style="margin-left:37px">mva</span><span class="fmt" style="margin-left:37px">Other popular music files</span>
    <div class="track-votes"><span><svg class="icon" width="11" height="11"><use href="#i-like"/></svg>Like</span><span><svg class="icon" width="11" height="11"><use href="#i-dislike"/></svg>Dislike</span><span><svg class="icon" width="11" height="11"><use href="#i-down"/></svg>Download</span></div>
  </div>
  <div class="track" style="top:336px">
    <span class="note"><svg class="icon" width="22" height="22"><use href="#i-note"/></svg></span>
    <div class="track-info"><div class="track-name">Nihil molestiae consequatur</div><div class="track-artist"><svg class="icon" width="9" height="9"><use href="#i-mic"/></svg>J. Marlow</div></div>
    <span class="sep"></span>
    <span class="fmt" style="margin-left:20px">Mp3</span><span class="fmt" style="margin-left:37px">mva</span><span class="fmt" style="margin-left:37px">Other popular music files</span>
    <div class="track-votes"><span><svg class="icon" width="11" height="11"><use href="#i-like"/></svg>Like</span><span><svg class="icon" width="11" height="11"><use href="#i-dislike"/></svg>Dislike</span><span><svg class="icon" width="11" height="11"><use href="#i-down"/></svg>Download</span></div>
  </div>
  <span class="view-more" style="left:958px;top:414px">View More &gt;&gt;</span>
</section>

<section class="section albums">
  <h2 class="section-title">LATEST <span class="accent">ALBUM</span></h2>
  <div class="album" style="left:98px"><div class="album-photo" role="img" aria-label="Band performing on a lit stage"></div><div class="album-caption">Molestiae Consequatur<span class="album-count"><svg class="icon" width="11" height="11"><use href="#i-cam"/></svg>14</span></div></div>
  <div class="album" style="left:354px"><div class="album-photo" role="img" aria-label="Group of young singers performing together"></div><div class="album-caption">Molestiae Consequatur<span class="album-count"><svg class="icon" width="10" height="10"><use href="#i-note"/></svg>14</span></div></div>
  <div class="album" style="left:608px"><div class="album-photo" role="img" aria-label="Singer in a red gown on a concert hall stage"></div><div class="album-caption">Molestiae Consequatur<span class="album-count"><svg class="icon" width="11" height="11"><use href="#i-cam"/></svg>14</span></div></div>
  <div class="album" style="left:864px"><div class="album-photo" role="img" aria-label="Guitarist playing under pink stage lights"></div><div class="album-caption">Molestiae Consequatur<span class="album-count"><svg class="icon" width="10" height="10"><use href="#i-note"/></svg>14</span></div></div>
</section>

<section class="section videos">
  <h2 class="section-title">VIDEO FILES OF <span class="accent">VIBRA</span></h2>
  <article class="vcard big">
    <div class="vcard-photo" role="img" aria-label="Rock singer performing at a microphone with a drummer behind"></div>
    <div class="vbody">
      <h4>Finibus Bonorum et Malorum Nam</h4>
      <div class="vmeta"><svg class="icon" width="10" height="10"><use href="#i-user"/></svg>Lena Torvik<span class="votes"><svg class="icon" width="10" height="10"><use href="#i-like"/></svg><svg class="icon" width="10" height="10"><use href="#i-dislike"/></svg></span></div>
      <p class="vtext">Et harum quidem rerum facilis est et expedita distinctio Et harum quidem rerum</p>
      <div class="tags"><span>MP4</span><span>WMV</span><span>DIVX</span><span>Others</span></div>
      <div class="vdl">Download now <svg class="icon" width="16" height="16"><use href="#i-down"/></svg></div>
    </div>
  </article>
  <article class="vcard small one" style="top:121px">
    <div class="vcard-photo" role="img" aria-label="Woman singing into a microphone"></div>
    <div class="vbody">
      <h4>Finibus Bonorum et Malorum Nam</h4>
      <div class="vmeta"><svg class="icon" width="10" height="10"><use href="#i-user"/></svg>Lena Torvik<span class="votes"><svg class="icon" width="10" height="10"><use href="#i-like"/></svg><svg class="icon" width="10" height="10"><use href="#i-dislike"/></svg></span></div>
      <p class="vtext">Et harum quidem rerum facilis est et expedita distinctio<br>Et harum quidem rerum est et expedita</p>
      <div class="vrow"><div class="tags"><span>MP4</span><span>WMV</span><span>DIVX</span><span>Others</span></div><div class="vdl">Download now <svg class="icon" width="14" height="14"><use href="#i-down"/></svg></div></div>
    </div>
  </article>
  <article class="vcard small two" style="top:269px">
    <div class="vcard-photo" role="img" aria-label="Woman listening to headphones"></div>
    <div class="vbody">
      <h4>Finibus Bonorum et Malorum Nam</h4>
      <div class="vmeta"><svg class="icon" width="10" height="10"><use href="#i-user"/></svg>Lena Torvik<span class="votes"><svg class="icon" width="10" height="10"><use href="#i-like"/></svg><svg class="icon" width="10" height="10"><use href="#i-dislike"/></svg></span></div>
      <p class="vtext">Et harum quidem rerum facilis est et expedita distinctio<br>Et harum quidem rerum est et expedita</p>
      <div class="vrow"><div class="tags"><span>MP4</span><span>WMV</span><span>DIVX</span><span>Others</span></div><div class="vdl">Download now <svg class="icon" width="14" height="14"><use href="#i-down"/></svg></div></div>
    </div>
  </article>
  <span class="view-more" style="left:992px;top:415px">View More &gt;&gt;</span>
</section>

<footer class="section footer">
  <nav class="footer-nav">
    <a href="#">Home</a><i>|</i><a href="#">About Us</a><i>|</i><a href="#">Music Album</a><i>|</i><a href="#">Video Album</a><i>|</i><a href="#">Gallery</a><i>|</i><a href="#">Contact Us</a>
  </nav>
  <div class="social"><span></span><span></span><span></span><span></span></div>
  <p class="copyright">Copyrights@2016Tunehall . All rights reserved</p>
  <div class="footer-line"></div>
</footer>
</body>
</html>
```